Business card and stationary for consulting business

We need business cards and matching stationary for professional consulting business for employment and human resources issues.
One of the CraftHive designers designed the logo with our company name.  Use the colors in the logo and may use light yellow as an accent color.
Add
Mara T. Vollen, J.D., LL.M.
485 E. Callister Lane
Winter Park, Florida  32789
407-555-0183
maravollenjd@quillpost.example

Industry/Entity Type
Business

```html
<!DOCTYPE html>
<html lang="en">
<head>
<meta charset="utf-8">
<title>Lumen HR — Business Card</title>
<link rel="stylesheet" href="https://fonts.googleapis.com/css2?family=Montserrat:wght@400&family=Arimo:wght@400;700&display=swap">
<style>
  :root {
    --band-dark: #0580ad;
    --paper: #ffffff;
    --field-top: #0190c9;
    --field-bottom: #00aeea;
    --brand-ink: #1a6a8c;
    --tagline-ink: #2a6d8f;
    --divider: #cfd3d6;
    --light-text: #ffffff;
  }
  html, body {
    margin: 0;
    padding: 0;
    width: 1200px;
    height: 686px;
    overflow: hidden;
    background: var(--paper);
  }
  .card {
    position: relative;
    width: 1200px;
    height: 686px;
    overflow: hidden;
    background: var(--paper);
  }
  .top-band {
    position: absolute;
    left: 0; top: 0;
    width: 1200px; height: 43px;
    background: var(--band-dark);
  }
  .brand-row {
    position: absolute;
    left: 0; top: 43px;
    width: 1200px; height: 214px;
  }
  .brand-name {
    position: absolute;
    left: 251px; top: 52px;
    margin: 0;
    font-family: "Montserrat", sans-serif;
    font-weight: 400;
    font-size: 76px;
    line-height: 1;
    letter-spacing: -1px;
    color: var(--brand-ink);
    white-space: nowrap;
  }
  .brand-divider {
    position: absolute;
    left: 681px; top: 29px;
  }
  .tagline {
    position: absolute;
    left: 702px; top: 57px;
    margin: 0; padding: 0;
    list-style: none;
    font-family: "Montserrat", sans-serif;
    font-weight: 400;
    font-size: 26px;
    line-height: 34px;
    color: var(--tagline-ink);
    white-space: nowrap;
  }
  .contact-field {
    position: absolute;
    left: 0; top: 257px;
    width: 1200px; height: 429px;
    background: linear-gradient(180deg, var(--field-top) 0%, var(--field-bottom) 100%);
  }
  .person-name {
    position: absolute;
    left: 48px; top: 192px;
    margin: 0;
    font-family: "Arimo", Arial, sans-serif;
    font-weight: 700;
    font-size: 30px;
    letter-spacing: 1px;
    text-transform: uppercase;
    color: var(--light-text);
    white-space: nowrap;
  }
  .contact-details {
    position: absolute;
    left: 672px; top: 137px;
    margin: 0;
    font-family: "Arimo", Arial, sans-serif;
    font-weight: 400;
    font-style: normal;
    font-size: 27px;
    line-height: 35px;
    color: var(--light-text);
    white-space: nowrap;
  }
  .contact-details span { display: block; }
</style>
</head>
<body>
  <main class="card">
    <div class="top-band"></div>

    <header class="brand-row">
      <h1 class="brand-name">Lumen HR</h1>
      <svg class="brand-divider" width="4" height="157" viewBox="0 0 4 157" aria-hidden="true">
        <rect x="0" y="0" width="3" height="157" fill="var(--divider)"/>
      </svg>
      <ul class="tagline">
        <li>Enhance Revenue</li>
        <li>Manage Expenses</li>
        <li>Protect Profit</li>
      </ul>
    </header>

    <section class="contact-field">
      <p class="person-name">Mara T. Vollen, J.D., LL.M.</p>
      <address class="contact-details">
        <span>Address: 485 E. Callister Lane</span>
        <span>Larkspur Bay, Florida 32841</span>
        <span>Tel. No.: 407-555-0183</span>
        <span>Email: maravollenjd@quillpost.example</span>
      </address>
    </section>
  </main>
</body>
</html>
```